Makeup Artist

Hi I am makeup artist I attached the business card that I found on the net love the design.
I would love something like this simple but looking expensive.
I want double side business card. Front my full name. my phone number, email address and facebook and my next appointment is... on the other side.
Thank you :)

Hello I change my Facebook account - Makeup by Liora, if you could please update your designs , thank you

Target Market(s)

high end clientele

Industry/Entity Type

Business

Colors
ec2027
ffc214
33b7a4
6b449b
e34197
9bcb3c
f37122
a64599

Requirements
Must have
• bright colours
Should not have
• brushes or whole lipsticks

```html
<!DOCTYPE html>
<html lang="en">
<head>
<meta charset="utf-8">
<title>Liora Vasenko – Makeup Artist Business Card</title>
<link rel="stylesheet" href="https://fonts.googleapis.com/css2?family=Quicksand:wght@300;400&family=Caveat+Brush&display=swap">
<style>
  :root {
    --paper: #ffffff;
    --ink: #1f1f1f;
    --ink-soft: #333333;
    --lipstick: #c8101e;
    --lipstick-bright: #ec2027;
    --lipstick-deep: #8e0a14;
    --card-light: #f4f4f4;
    --card-mid: #c9c9c9;
    --card-edge: #747474;
  }
  * { margin: 0; padding: 0; box-sizing: border-box; }
  html, body {
    width: 1200px;
    height: 1110px;
    overflow: hidden;
    background: var(--paper);
  }
  .canvas {
    position: relative;
    width: 1200px;
    height: 1110px;
    background: var(--paper);
  }

  /* Contact side */
  .contact-side { position: absolute; left: 190px; top: 138px; }
  .contact-list { list-style: none; }
  .contact-item {
    display: flex;
    align-items: center;
    font-family: "Quicksand", sans-serif;
    font-weight: 300;
    color: var(--ink);
    letter-spacing: 1px;
    line-height: 1;
  }
  .contact-item--phone { font-size: 27px; height: 38px; }
  .contact-item--social,
  .contact-item--email { font-size: 34px; height: 44px; letter-spacing: 1.5px; }
  .contact-icon {
    width: 22px;
    height: 22px;
    margin-right: 12px;
    flex: none;
  }
  .social-dot {
    width: 20px;
    height: 20px;
    border-radius: 50%;
    background: var(--ink);
    margin: 0 13px 0 2px;
    flex: none;
  }
  .appointment-note {
    margin: 26px 0 0 32px;
    font-family: "Caveat Brush", cursive;
    font-size: 40px;
    color: var(--lipstick-bright);
    letter-spacing: 2px;
    transform: skewX(-6deg);
    transform-origin: left;
  }

  /* Name side */
  .name-side {
    position: absolute;
    left: 258px;
    top: 638px;
    width: 942px;
    height: 472px;
    background: radial-gradient(ellipse 60% 70% at 52% 58%, var(--card-light) 0%, var(--card-mid) 55%, var(--card-edge) 100%);
    overflow: hidden;
  }
  .lipstick-swatch {
    position: absolute;
    left: 50px;
    top: 24px;
    width: 292px;
    height: 394px;
  }
  .artist-name {
    position: absolute;
    right: 90px;
    top: 180px;
    font-family: "Caveat Brush", cursive;
    font-size: 84px;
    font-weight: 400;
    color: var(--lipstick);
    letter-spacing: 7px;
    white-space: nowrap;
  }
  .artist-title {
    position: absolute;
    right: 92px;
    top: 279px;
    font-family: "Quicksand", sans-serif;
    font-weight: 400;
    font-size: 34px;
    color: var(--ink-soft);
    letter-spacing: 2px;
  }
</style>
</head>
<body>
<main class="canvas">

  <section class="contact-side" aria-label="Card back with contact details">
    <ul class="contact-list">
      <li class="contact-item contact-item--phone">
        <svg class="contact-icon" viewBox="0 0 24 24" aria-hidden="true">
          <circle cx="12" cy="12" r="10.5" fill="none" stroke="#1f1f1f" stroke-width="1.6"/>
          <path d="M8.6 6.8c.5-.4 1.1-.3 1.4.2l1 1.7c.3.5.1 1-.3 1.3l-.7.5c.6 1.4 1.6 2.5 3 3.2l.6-.7c.4-.4.9-.5 1.3-.2l1.7 1c.5.3.6 1 .2 1.4l-.8.9c-.6.6-1.6.7-2.6.3-2.6-1.1-4.6-3.2-5.6-5.8-.4-1-.2-2 .4-2.6z" fill="#1f1f1f"/>
        </svg>
        <span>0421550193</span>
      </li>
      <li class="contact-item contact-item--social">
        <span class="social-dot" aria-hidden="true"></span>
        <span>Makeup by Liora</span>
      </li>
      <li class="contact-item contact-item--email">
        <svg class="contact-icon" viewBox="0 0 24 24" aria-hidden="true">
          <rect x="2" y="6" width="20" height="14" fill="#1f1f1f"/>
          <path d="M2 6l10 8 10-8" fill="none" stroke="#ffffff" stroke-width="1.6"/>
        </svg>
        <span>lioravasenko@mailpost.com</span>
      </li>
    </ul>
    <p class="appointment-note">Looking forward to our appointment !</p>
  </section>

  <section class="name-side" aria-label="Card front with name">
    <svg class="lipstick-swatch" viewBox="0 0 292 394" role="img" aria-label="Photo of a red lipstick tip and a smeared lipstick swatch">
      <defs>
        <linearGradient id="swatchTone" x1="0" y1="0" x2="1" y2="1">
          <stop offset="0" stop-color="#e0202b"/>
          <stop offset="0.6" stop-color="#c8101e"/>
          <stop offset="1" stop-color="#8e0a14"/>
        </linearGradient>
      </defs>
      <rect x="0" y="0" width="292" height="394" rx="60" fill="url(#swatchTone)"/>
    </svg>
    <h1 class="artist-name">Liora Vasenko</h1>
    <p class="artist-title">Makeup Artist</p>
  </section>

</main>
</body>
</html>
```